Larkspur Ridge Management - Business Cards

I need business cards. My current logo was designed by a designer at this site and I very much like and am happy with the results. I would like a business card that is trendy, unique, current yet professional. I deal with high net worth clients daily

Target Market(s)

Out of state investors looking to get into the rental market in Ohio

Industry/Entity Type

Property Management, Consulting

Contact Information for Business Card

Name, Title (Chief Financial Officer) office phone number (555) 817-3094 website address larkridgemgmt.example

Font styles to use
Sans Serif

Colors
0054AA
0677BA
7BADD7
CADEEF
E8F1F8
0094D4
00A9DD
6FCCEA
C7EBF8
E9F6FB
00AB8E
00BBA5
67D7C9
C6EFE9
E9F9F6

```html
<!DOCTYPE html>
<html lang="en">
<head>
<meta charset="utf-8">
<title>Larkspur Ridge Management – Business Cards</title>
<link rel="stylesheet" href="https://fonts.googleapis.com/css2?family=Montserrat:wght@800&family=Poppins:wght@400;600&display=swap">
<style>
  :root {
    --backdrop: #1e1e1f;
    --card-white: #f4f7f9;
    --brand-blue: #0054aa;
    --brand-blue-mid: #0677ba;
    --brand-teal: #00ab8e;
    --brand-teal-light: #67d7c9;
    --rule: #7badd7;
    --on-blue: #ffffff;
  }
  * { box-sizing: border-box; margin: 0; padding: 0; }
  html, body {
    width: 1200px; height: 900px; overflow: hidden;
    background: var(--backdrop);
    font-family: "Poppins", sans-serif;
  }
  .sheet { position: relative; width: 1200px; height: 900px; }

  .card {
    position: absolute; top: 295px;
    width: 540px; height: 310px;
    border-radius: 22px;
    border-bottom: 7px solid var(--brand-teal);
    overflow: hidden;
  }
  .card--front { left: 40px; background: var(--card-white); }
  .card--back { left: 620px; background: var(--brand-blue); }

  .brand {
    position: absolute; display: flex; align-items: center; gap: 12px;
    font-family: "Poppins", sans-serif; font-weight: 600;
  }
  .brand__square { width: 18px; height: 18px; flex: none; background: var(--brand-teal); }
  .brand__name { font-size: 20px; line-height: 1.2; }

  .card--front .brand { left: 34px; top: 110px; width: 196px; color: var(--brand-blue); }

  .divider {
    position: absolute; left: 240px; top: 62px;
    width: 1px; height: 180px; background: var(--rule);
  }

  .identity { position: absolute; left: 266px; right: 30px; top: 72px; }
  .identity__name {
    font-family: "Montserrat", sans-serif; font-weight: 800;
    font-size: 20px; color: var(--brand-blue); letter-spacing: 0.2px;
    white-space: nowrap;
  }
  .identity__title { font-size: 14px; color: var(--brand-teal); margin-top: 2px; }

  .contacts { position: absolute; left: 266px; right: 30px; top: 150px; list-style: none; }
  .contacts li {
    display: flex; align-items: center; gap: 9px;
    font-size: 13px; color: var(--brand-blue-mid); line-height: 1.85;
    white-space: nowrap;
  }
  .contacts svg { width: 13px; height: 13px; flex: none; }
  .contacts .accent { color: var(--brand-teal); }

  .card--back .brand {
    left: 0; right: 0; top: 0; bottom: 0; justify-content: center;
    color: var(--on-blue);
  }
  .card--back .brand__square { background: var(--brand-teal-light); }
  .card--back .brand__name { font-size: 24px; max-width: 250px; }
</style>
</head>
<body>
<main class="sheet">
  <section class="card card--front">
    <div class="brand">
      <span class="brand__square"></span>
      <span class="brand__name">Larkspur Ridge Management</span>
    </div>
    <div class="divider"></div>
    <div class="identity">
      <h1 class="identity__name">DANIEL WHITCOMB</h1>
      <p class="identity__title">Chief Financial Officer</p>
    </div>
    <ul class="contacts">
      <li>
        <svg viewBox="0 0 16 16" aria-hidden="true"><path fill="#00ab8e" d="M3.6 1.5l2.2 2.6-1.3 1.6c.9 2 2.4 3.5 4.4 4.4l1.6-1.3 2.6 2.2-1.4 2.1C6.5 13.2 2.8 9.5 1.9 4.3z"/></svg>
        <span>(555) 817-3094</span>
      </li>
      <li>
        <svg viewBox="0 0 16 16" aria-hidden="true"><rect x="1" y="3.5" width="14" height="9" fill="#00ab8e"/><path d="M1.5 4l6.5 5 6.5-5" fill="none" stroke="#f4f7f9" stroke-width="1.3"/></svg>
        <span>info@larkridgemgmt.example</span>
      </li>
      <li>
        <svg viewBox="0 0 16 16" aria-hidden="true"><g fill="none" stroke="#00ab8e" stroke-width="1.4"><circle cx="8" cy="8" r="6.3"/><ellipse cx="8" cy="8" rx="2.8" ry="6.3"/><path d="M1.7 8h12.6M2.8 4.8h10.4M2.8 11.2h10.4"/></g></svg>
        <span>www.<span class="accent">larkridgemgmt.example</span></span>
      </li>
    </ul>
  </section>

  <section class="card card--back">
    <div class="brand">
      <span class="brand__square"></span>
      <span class="brand__name">Larkspur Ridge Management</span>
    </div>
  </section>
</main>
</body>
</html>
```